Design for LED christmas lights

📦 Packaging Briefing – Christmas Lights (Glowra)
First design for approval – Product: 360 LED Warm White String Lights – Connectable, 8 Functions, IP44, EU Plug
🧩 Project Overview:
We are developing 6 unique box styles for the Glowra Christmas lighting range, covering 11 design variations (e.g. LED counts, lengths, plug types). This briefing is for the initial box design to be created for internal approval, based on the yellow-highlighted product in the provided Excel file.
✅ Design Style:
Use the same layout, typography, and structure as the attached LED bulb box.
The font and overall style must remain consistent with that example.
Only adjust layout elements as needed to accommodate Christmas light visuals and product-specific features.
📌 Box Content (for this product):
Product Name (front and sides):
360 LED Warm White String Lights – Connectable, 8 Functions, IP44, EU Plug
Highlight these features (icons or bullet format):
360 LEDs
Warm White
Connectable
8 Functions
IP44 (outdoor suitable)
EU Plug
Also include:
CE logo
EAN barcode (from Excel file)
Article number (from Excel file)
🖼 Visuals:
Use the corresponding product image from the Excel file.
Integrate image into the layout similarly to how the LED bulb is shown on its box (clean placement, no background clutter).
🏷 Brand & Company Info:
Brand/logo: Glowra (see attached logo file)
Company name: Far Beyond Dusk B.V.
Email: info@verderdanschemer.nl
Phone: +31 487 5921
🎨 Tone & Feel:
Clean, professional, and slightly festive – think minimal Christmas warmth, not overly decorative
Style should match the LED bulb box to build a coherent product line

```html
<!DOCTYPE html>
<html lang="en">
<head>
<meta charset="utf-8">
<title>Glowra – 360 LED Warm White String Lights box</title>
<link href="https://fonts.googleapis.com/css2?family=Barlow:wght@300;500;700;800&display=swap" rel="stylesheet">
<style>
  :root {
    --bg: #d3e1e8;
    --charcoal: #474747;
    --charcoal-deep: #3c3c3c;
    --amber: #f4a62a;
    --amber-light: #fbb83f;
    --white: #ffffff;
    --glow: #ffe2a0;
  }
  * { box-sizing: border-box; margin: 0; padding: 0; }
  html, body { width: 1056px; height: 1200px; overflow: hidden; }
  body {
    background: var(--bg);
    font-family: 'Barlow', 'Helvetica Neue', Arial, sans-serif;
    position: relative;
  }
  .panel { position: absolute; overflow: hidden; }

  /* Top panel */
  .top-panel {
    left: 358px; top: 250px; width: 640px; height: 250px;
    background: var(--charcoal);
  }
  .top-panel .brand {
    position: absolute; left: 0; right: 0; top: 38px;
    text-align: center; color: var(--amber);
    font-weight: 300; font-size: 56px; letter-spacing: 18px;
  }
  .top-panel .title-pill {
    position: absolute; left: 70px; top: 130px; width: 420px; height: 60px;
    background: var(--amber); border-radius: 14px;
    display: flex; align-items: center; gap: 16px; padding-left: 26px;
  }
  .title-pill .count { color: var(--white); font-weight: 800; font-size: 44px; }
  .title-pill .desc {
    color: var(--white); font-weight: 500; font-size: 15px; line-height: 1.05; letter-spacing: 1px;
  }
  .top-panel .length {
    position: absolute; right: 40px; top: 150px; text-align: center;
    color: #222; font-weight: 500;
  }
  .length .num { font-size: 30px; display: block; line-height: 1; }
  .length .unit { font-size: 15px; letter-spacing: 1px; }

  /* Side panel */
  .side-panel {
    left: 58px; top: 500px; width: 300px; height: 450px;
    background: var(--charcoal);
    padding: 44px 30px;
    color: var(--amber);
  }
  .side-panel .brand {
    font-weight: 300; font-size: 40px; letter-spacing: 10px; margin-bottom: 28px;
  }
  .side-panel .company { font-weight: 700; font-size: 17px; line-height: 1.35; }
  .side-panel .contact { font-size: 16px; line-height: 1.4; font-weight: 500; }
  .side-panel .disposal { font-size: 16px; line-height: 1.35; margin-top: 16px; font-weight: 500; }
  .side-panel .marks {
    position: absolute; left: 30px; bottom: 40px; display: flex; gap: 22px; align-items: center;
  }
  .marks .mark { width: 40px; height: 40px; border: 3px solid var(--white); border-radius: 4px; }
  .marks .mark.round { border-radius: 50%; }

  /* Front panel */
  .front-panel {
    left: 358px; top: 500px; width: 640px; height: 450px;
    background: linear-gradient(165deg, var(--amber-light) 0%, var(--amber) 45%, #8c6a3a 75%, var(--charcoal) 100%);
  }
  .front-panel .brand {
    position: absolute; left: 80px; top: 48px;
    color: var(--white); font-weight: 300; font-size: 86px; letter-spacing: 22px;
  }
  .front-panel .product-visual {
    position: absolute; left: 60px; top: 170px; width: 280px; height: 210px;
    border-radius: 50%;
    background: radial-gradient(circle at 50% 50%, #2f3a2c 0 18%, var(--glow) 30%, #f3c56a 60%, rgba(244,166,42,0) 72%);
  }
  .front-panel .features {
    position: absolute; right: 26px; top: 150px; width: 230px; height: 215px;
    background: var(--amber); border-radius: 10px;
    padding: 26px 20px 0 28px; list-style: none;
  }
  .features li {
    color: var(--white); font-weight: 500; font-size: 21px; line-height: 1.45; letter-spacing: 0.5px;
  }
  .features li::before { content: "•"; margin-right: 12px; }
  .front-panel .product-band {
    position: absolute; left: 0; right: 0; bottom: 0; height: 62px;
    background: var(--amber);
    display: flex; align-items: center; padding-left: 26px;
    color: var(--charcoal-deep); font-weight: 800; font-size: 31px; letter-spacing: 1px;
  }
</style>
</head>
<body>

<section class="panel top-panel">
  <div class="brand">GLOWRA</div>
  <div class="title-pill">
    <span class="count">360 LED</span>
    <span class="desc">WARM WHITE<br>STRING LIGHTS</span>
  </div>
  <div class="length"><span class="num">12</span><span class="unit">METER</span></div>
</section>

<section class="panel side-panel">
  <div class="brand">GLOWRA</div>
  <p class="company">Far Beyond Dusk B.V.</p>
  <p class="contact">+31 487 5921<br>info@verderdanschemer.nl<br>www.verderdanschemer.nl</p>
  <p class="disposal">This product shall not be disposed of as unsorted municipal waste.</p>
  <div class="marks">
    <span class="mark round" aria-label="Certification mark"></span>
    <span class="mark" aria-label="Waste disposal mark"></span>
    <span class="mark" aria-label="Litter bin mark"></span>
    <span class="mark round" aria-label="Recycling mark"></span>
  </div>
</section>

<section class="panel front-panel">
  <div class="brand">GLOWRA</div>
  <div class="product-visual" role="img" aria-label="Photo of coiled glowing warm white LED string lights with plug and adapter"></div>
  <ul class="features">
    <li>360 LEDS</li>
    <li>WARM WHITE</li>
    <li>CONNECTABLE</li>
    <li>8 FUNCTIONS</li>
    <li>IP44</li>
    <li>EU PLUG</li>
  </ul>
  <div class="product-band">360 LED WARM WHITE STRING LIGHTS</div>
</section>

</body>
</html>
```